Banners Ads for Marketing Company

We are looking to have banner ads designed that will carry a common theme to be used across the following sizes (all these sizes will need to be created): 468 x 60, 728 x 90, 250 x 250, 300 x 250, 120 x 600, 160 x 600.

We are a leading SEO firm. We are often featured in Valcrest, Marketwright, The Pellmoor Ledger, Query Signal Digest, Crawlpath Review Daily, etc for our SEO expertise. We have hundreds of clients and we are recognized by Rankvane.com, Finestagencylist.com, Agencyratingshub.com, and Outreachplaza.com as one of the top SEO firms in the U.S.

The goal of our campaign is to get business professional to click on these ads to get more information about who we are and request a quote. We will be using these ads for retargeting campaigns as well as regular display campaigns. The banners need to be clean and crisp and get people into our sales funnel.

Our website is: http://www.brightlanterndigital.com/

```html
<!DOCTYPE html>
<html lang="en">
<head>
<meta charset="utf-8">
<title>Bright Lantern Digital – Animated Banner Frames</title>
<link rel="stylesheet" href="https://fonts.googleapis.com/css2?family=Arimo:wght@400;700&display=swap">
<style>
  :root {
    --navy: #0e1a35;
    --navy-text: #0f1a33;
    --gold-light: #f7e6ac;
    --gold: #e6c670;
    --gold-deep: #b88f3e;
    --brown: #7a582a;
    --orange: #f7941d;
    --orange-light: #ffb347;
    --orange-deep: #e8720c;
    --arrow-circle: #5a2f0c;
    --stripe-red: #a8332c;
    --stripe-white: #ffffff;
    --page: #ffffff;
    --label: #0f1a33;
  }
  html, body {
    margin: 0;
    padding: 0;
    width: 1200px;
    height: 1200px;
    overflow: hidden;
    background: var(--page);
    font-family: "Arimo", Arial, sans-serif;
  }
  .canvas {
    position: relative;
    width: 1200px;
    height: 1200px;
  }
  .frame-label {
    position: absolute;
    left: 21px;
    font-size: 28px;
    color: var(--label);
    line-height: 1;
  }
  .banner {
    position: absolute;
    left: 157px;
    width: 1027px;
    height: 127px;
    display: block;
  }
  .style-title {
    position: absolute;
    left: 0;
    width: 1328px;
    top: 722px;
    text-align: center;
    font-size: 57px;
    color: var(--label);
    line-height: 1;
  }
  .logo-name { font-family: "Arimo", Arial, sans-serif; font-weight: 400; fill: #ffffff; }
  .headline { font-family: "Arimo", Arial, sans-serif; font-weight: 700; fill: var(--brown); }
  .offer-title { font-family: "Arimo", Arial, sans-serif; font-weight: 700; fill: var(--navy-text); }
  .offer-item { font-family: "Arimo", Arial, sans-serif; font-weight: 700; fill: var(--brown); }
  .cta-text { font-family: "Arimo", Arial, sans-serif; font-weight: 700; fill: var(--arrow-circle); }
</style>
</head>
<body>
<div class="canvas">

  <svg width="0" height="0" style="position:absolute" aria-hidden="true">
    <defs>
      <radialGradient id="bulb-glow" cx="0.5" cy="0.5" r="0.5">
        <stop offset="0" stop-color="#e9eef5"/>
        <stop offset="0.35" stop-color="#8a98b0"/>
        <stop offset="1" stop-color="#0e1a35" stop-opacity="0"/>
      </radialGradient>
      <linearGradient id="ribbon-fill" x1="0" y1="0" x2="1" y2="0">
        <stop offset="0" stop-color="#e3c064"/>
        <stop offset="0.45" stop-color="#f8e8b0"/>
        <stop offset="1" stop-color="#e2c06a"/>
      </linearGradient>
      <linearGradient id="tail-fill" x1="0" y1="0" x2="0" y2="1">
        <stop offset="0" stop-color="#f3dc96"/>
        <stop offset="1" stop-color="#e2bf66"/>
      </linearGradient>
      <linearGradient id="cta-fill" x1="0" y1="0" x2="0" y2="1">
        <stop offset="0" stop-color="#ffbf5a"/>
        <stop offset="0.5" stop-color="#f7941d"/>
        <stop offset="1" stop-color="#e8720c"/>
      </linearGradient>
      <linearGradient id="arc-fill" x1="0" y1="0" x2="1" y2="0">
        <stop offset="0" stop-color="#f7941d"/>
        <stop offset="1" stop-color="#ffc45a"/>
      </linearGradient>

      <g id="banner-base">
        <rect x="0" y="0" width="728" height="90" fill="var(--navy)"/>
        <rect x="215" y="55" width="513" height="30" fill="var(--stripe-white)"/>
        <rect x="215" y="84" width="513" height="6" fill="var(--stripe-red)"/>
        <circle cx="190" cy="44" r="46" fill="url(#bulb-glow)" role="img" aria-label="Glowing light bulb illustration"/>
        <path d="M204,0 L220,0 Q206,45 220,90 L204,90 Q190,45 204,0 Z" fill="url(#arc-fill)"/>
        <circle cx="20" cy="45" r="5" fill="var(--orange)"/>
        <text class="logo-name" x="30" y="50" font-size="12.5">brightlanterndigital.com</text>
        <polygon points="512,78 536,78 536,85 512,85" fill="var(--gold-deep)"/>
        <polygon points="530,18 556,18 548,50 582,84 530,84" fill="url(#tail-fill)"/>
        <rect x="218" y="6" width="318" height="72" fill="url(#ribbon-fill)"/>
        <polygon points="509,27 512,35 520,35 513.5,40 516,48 509,43 502,48 504.5,40 498,35 506,35" fill="var(--gold-deep)"/>
        <rect x="583" y="25" width="134" height="41" rx="3" fill="url(#cta-fill)"/>
        <text class="cta-text" x="592" y="51" font-size="16">Click Here</text>
        <circle cx="697" cy="45.5" r="15" fill="var(--arrow-circle)"/>
        <path d="M693,38.5 L700,45.5 L693,52.5" fill="none" stroke="#ffffff" stroke-width="3" stroke-linecap="round" stroke-linejoin="round"/>
      </g>
    </defs>
  </svg>

  <div class="frame-label" style="top:340px;">Frame A</div>
  <svg class="banner banner-frame-a" style="top:285px;" viewBox="0 0 728 90" role="img" aria-label="Banner frame A: Need Visibility? We Are Your Marketing Firm">
    <use href="#banner-base"/>
    <text class="headline" x="237" y="38" font-size="27">Need Visibility?</text>
    <text class="headline" x="239" y="57" font-size="16">We Are Your Marketing Firm</text>
  </svg>

  <div class="frame-label" style="top:488px;">Frame B</div>
  <svg class="banner banner-frame-b" style="top:433px;" viewBox="0 0 728 90" role="img" aria-label="Banner frame B: We Are A leading SEO Firm">
    <use href="#banner-base"/>
    <text class="headline" x="360" y="35" font-size="24" text-anchor="middle">We Are A leading</text>
    <text class="headline" x="360" y="58" font-size="24" text-anchor="middle">SEO Firm</text>
  </svg>

  <div class="frame-label" style="top:626px;">Frame C</div>
  <svg class="banner banner-frame-c" style="top:576px;" viewBox="0 0 728 90" role="img" aria-label="Banner frame C: What We Offer">
    <use href="#banner-base"/>
    <text class="offer-title" x="241" y="22" font-size="16">What We Offer</text>
    <line x1="238" y1="27" x2="530" y2="27" stroke="var(--navy-text)" stroke-width="1"/>
    <text class="offer-item" x="241" y="45" font-size="13.5">SEO</text>
    <text class="offer-item" x="241" y="63" font-size="13.5">Pay per Click</text>
    <text class="offer-item" x="364" y="45" font-size="13.5">Web Design</text>
    <text class="offer-item" x="364" y="63" font-size="13.5">Email Marketing</text>
  </svg>

  <div class="style-title">Animated Style</div>
</div>
</body>
</html>
```